Need a business letterhead for word docs

Hi, I need a business letterhead. We have had some before but they have issues printing them. I have attached a sample of what we have used that I want improved :) and a PSD of our logo, please use the one with all caps. This will be used for all our correspondance with clients and profeesionals. Our client base are children, so these documents will go to their parents and doctors and paediatricians who also treat these children.

Target Market(s)

Clients (who are families and children) and doctors/paediatricians

Industry/Entity Type

Health Care

Font styles to use
Sans Serif

Colors
85cae6

Requirements
Must have
• My logo and the feel of my logo
Nice to have
• clean feel

```html
<!DOCTYPE html>
<html lang="en">
<head>
<meta charset="utf-8">
<title>Bright Path Letterhead</title>
<link rel="stylesheet" href="https://fonts.googleapis.com/css2?family=Fira+Sans:ital,wght@0,600;1,400&display=swap">
<style>
  :root {
    --brand-blue: #0288d1;
    --brand-sky: #85cae6;
    --band-grey: #5d5d5d;
    --text-grey: #4a4a4a;
    --rule-grey: #666666;
    --paper: #ffffff;
    --wash: #eef6fb;
  }
  html, body {
    margin: 0;
    padding: 0;
    overflow: hidden;
    background: var(--paper);
  }
  .letterhead {
    position: relative;
    width: 927px;
    height: 1200px;
    background: var(--paper);
    overflow: hidden;
    font-family: "Fira Sans", Arial, sans-serif;
  }
  .side-band {
    position: absolute;
    top: 0;
    right: 0;
    width: 44px;
    height: 1200px;
  }
  .brand-wash {
    position: absolute;
    left: 0;
    top: 400px;
    width: 600px;
    height: 800px;
    background: radial-gradient(ellipse at 30% 55%, var(--wash) 0%, rgba(238,246,251,0.5) 45%, rgba(255,255,255,0) 75%);
  }
  .brand-name {
    position: absolute;
    right: 94px;
    top: 152px;
    margin: 0;
    font-weight: 600;
    font-size: 40px;
    letter-spacing: 0.5px;
    color: var(--brand-blue);
    line-height: 1;
  }
  .address-block {
    position: absolute;
    left: 717px;
    font-style: italic;
    font-size: 14px;
    line-height: 18px;
    color: var(--text-grey);
    margin: 0;
  }
  .address-main { top: 221px; }
  .address-centre { top: 268px; }
  .contact-block {
    position: absolute;
    left: 60px;
    right: 94px;
    top: 1103px;
    margin: 0;
    text-align: right;
    font-style: italic;
    font-size: 14px;
    line-height: 18px;
    color: var(--text-grey);
  }
  .contact-line {
    display: block;
  }
  .contact-email {
    display: flex;
    align-items: center;
    gap: 10px;
  }
  .footer-rule {
    flex: 1;
    height: 2px;
    margin-top: 2px;
    background: var(--rule-grey);
  }
</style>
</head>
<body>
  <div class="letterhead">
    <div class="brand-wash" role="img" aria-label="Faint brand decoration in pale blue and grey"></div>

    <svg class="side-band" viewBox="0 0 44 1200" aria-hidden="true">
      <polygon points="0,0 44,0 44,616 0,570" fill="var(--brand-blue)"/>
      <polygon points="0,584 44,630 44,1200 0,1200" fill="var(--band-grey)"/>
    </svg>

    <h1 class="brand-name">BRIGHT PATH</h1>

    <address class="address-block address-main">
      48 Fernley Grove<br>
      Hampton 3188
    </address>
    <address class="address-block address-centre">
      Therapy Centre<br>
      19 Alder St<br>
      Beaumaris 3193
    </address>

    <address class="contact-block">
      <span class="contact-line">Telephone: 03 9470 2615</span>
      <span class="contact-line">FAX: 03 9470 2617</span>
      <span class="contact-line contact-email"><span class="footer-rule"></span><span>E-mail: hello@brightpathclinic.com.au</span></span>
    </address>
  </div>
</body>
</html>
```